Einfache Webside für kleine Promotion- und Personalagentur
Zielgruppe
Lumo Staffing ist eine international tätige Promotion- und Personalagentur. Wir bieten auch im Bereich Sport der jew. Sportart affine Hostessen und Hosts f an.
Aufgabenstellung
Wir hatten bis dato eine sehr gute Auftragslage und leider keine Zeit für eine Homepage. Wir suchen jemaden der uns das Design für die Seite übernimmt und Online stellt. Wir sind auch offen wenn dies über z.B. Q+Z erfolgt. Auf den jeweiligen Seiten wollen wir den Text dann immer selbst eintragen. Seiten: Startseite mit Buttons zu folgenden Feldern: Promotion (Text mit Erklärung was wir machen und Bildern), Personal (Text mit Erklärung was wir machen und Bilder - die Bilder sollten austauschbar sein), Team, Referenzen, Kontaktseite, Gästebuch, Impressum. Die Seite sollte Modern aussehen und nicht zu überladen sein.

```html
<!DOCTYPE html>
<html lang="de">
<head>
<meta charset="utf-8">
<title>Lumo Staffing – International Promotion &amp; HR Services</title>
<link rel="stylesheet" href="https://fonts.googleapis.com/css2?family=Questrial&family=Jost:wght@400&display=swap">
<style>
  :root {
    --teal: #7ccbd6;
    --ink: #1b1b1b;
    --navy: #1e2a38;
    --white: #ffffff;
    --grey: #a7aaac;
    --hero-a: #5b4a4d;
    --hero-b: #8a8f8c;
    --hero-c: #2f4a5f;
  }
  * { box-sizing: border-box; margin: 0; padding: 0; }
  html, body { width: 1200px; height: 1148px; overflow: hidden; background: var(--white); }
  body { position: relative; font-family: "Jost", sans-serif; color: var(--ink); }

  .hero {
    position: absolute; left: 0; top: 0; width: 1200px; height: 264px;
    background: linear-gradient(100deg, var(--hero-a) 0%, var(--hero-b) 45%, #6f7c84 70%, var(--hero-c) 100%);
  }
  .hero-brand {
    position: absolute; left: 0; width: 1200px; top: 176px; text-align: center;
    font-family: "Questrial", sans-serif; color: var(--white);
  }
  .hero-brand .name { font-size: 40px; letter-spacing: 1px; line-height: 1; }
  .hero-brand .tagline { font-size: 16px; margin-top: 4px; }
  .hero-mark {
    position: absolute; left: 553px; top: 62px; width: 96px; height: 96px;
    border-radius: 50%; background: var(--white); opacity: .95;
  }

  .lang {
    position: absolute; left: 1101px; top: 19px; width: 99px; height: 30px;
    background: var(--teal); font-family: "Questrial", sans-serif; font-size: 16px;
    display: flex; align-items: center; justify-content: center; gap: 14px; color: var(--navy);
  }

  .nav {
    position: absolute; left: 0; top: 264px; width: 1200px; height: 41px; background: var(--teal);
    font-family: "Questrial", sans-serif; font-size: 18px; letter-spacing: 1px; color: var(--navy);
  }
  .nav-item { position: absolute; top: 0; height: 41px; line-height: 41px; }
  .nav-item.active { background: var(--white); padding: 0 17px; }
  .nav-badge {
    position: absolute; left: 100px; top: 242px; width: 84px; height: 84px; border-radius: 50%;
    background: var(--white); display: flex; align-items: center; justify-content: center;
    font-family: "Questrial", sans-serif; font-size: 12px; color: var(--teal); text-align: center;
  }

  .page-title {
    position: absolute; left: 131px; top: 362px; font-family: "Questrial", sans-serif;
    font-size: 31px; font-weight: 400;
  }
  .copy { position: absolute; font-size: 12px; line-height: 16px; }
  .copy p + p { margin-top: 16px; }
  .copy-intro { left: 129px; top: 432px; width: 490px; }
  .copy-second { left: 523px; top: 659px; width: 550px; }

  .photo { position: absolute; }
  .photo-team { left: 706px; top: 356px; width: 366px; height: 245px;
    background: linear-gradient(90deg, #8c949c, #e9e6e2 45%, #d8d4cf 70%, #7f8790); }
  .photo-event { left: 129px; top: 609px; width: 366px; height: 245px;
    background: linear-gradient(180deg, #d9dcdc 0%, #bfc3c4 55%, #c33a3e 88%, #000 95%); }

  .social { position: absolute; left: 129px; top: 935px; display: flex; gap: 8px; }
  .social span { width: 28px; height: 28px; border-radius: 50%; background: var(--navy); display: block; }
  .footer-links {
    position: absolute; right: 124px; top: 939px; font-size: 15px; display: flex; align-items: center; gap: 9px;
  }

  .footer {
    position: absolute; left: 0; top: 980px; width: 1200px; height: 168px; background: var(--navy);
    color: var(--white); font-size: 12px; line-height: 16px;
  }
  .footer-col { position: absolute; top: 45px; }
  .footer-rule { position: absolute; top: 48px; width: 2px; height: 82px; background: var(--teal); }
  .footer-brand {
    position: absolute; left: 976px; top: 42px; width: 96px; height: 96px; border-radius: 50%;
    border: 10px solid var(--grey); display: flex; align-items: center; justify-content: center;
    font-family: "Jost", sans-serif; font-size: 12px; color: var(--grey); text-align: center;
  }
</style>
</head>
<body>
  <header>
    <div class="hero" role="img" aria-label="Foto: Tablet mit Website, Tasse und Notizbuch auf Holztisch"></div>
    <div class="hero-mark" aria-hidden="true"></div>
    <div class="hero-brand">
      <div class="name">Lumo Staffing</div>
      <div class="tagline">International Promotion &amp; HR Services</div>
    </div>
    <div class="lang"><span>DE</span><span>I</span><span>EN</span></div>
  </header>

  <nav class="nav">
    <span class="nav-item active" style="left:232px">SERVICES</span>
    <span class="nav-item" style="left:400px">TEAM</span>
    <span class="nav-item" style="left:512px">REFERENZEN</span>
    <span class="nav-item" style="left:695px">KONTAKT</span>
    <span class="nav-item" style="left:841px">IMPRESSUM</span>
    <span class="nav-item" style="left:1010px">SUCHE</span>
  </nav>
  <div class="nav-badge">Lumo<br>Staffing</div>

  <main>
    <h1 class="page-title">International Promotion &amp; HR Services</h1>
    <div class="copy copy-intro">
      <p>Lorem ipsum dolor sit amet, consectetuer adipiscing elit. Aenean commodo ligula eget dolor. Aenean massa. Cum sociis natoque penatibus et magnis dis parturient montes, nascetur ridiculus mus.</p>
      <p>Donec quam felis, ultricies nec, pellentesque eu, pretium quis, sem. Nulla consequat massa quis enim. Donec pede justo, fringilla vel, aliquet nec, vulputate eget, arcu. In enim justo, rhoncus ut, imperdiet a, venenatis vitae, justo. Nullam dictum felis eu pede mollis pretium. Integer tincidunt. Cras dapibus. Vivamus elementum semper nisi. Aenean vulputate eleifend</p>
    </div>
    <div class="photo photo-team" role="img" aria-label="Foto: Geschäftsfrau mit Mappe vor Kollegen im Büroflur"></div>
    <div class="photo photo-event" role="img" aria-label="Foto: Besucher auf rotem Teppich in einem Veranstaltungssaal"></div>
    <div class="copy copy-second">
      <p>Lorem ipsum dolor sit amet, consectetuer adipiscing elit. Aenean commodo ligula eget dolor. Aenean massa. Cum sociis natoque penatibus et magnis dis parturient montes, nascetur ridiculus mus.</p>
      <p>Donec quam felis, ultricies nec, pellentesque eu, pretium quis, sem. Nulla consequat massa quis enim. Donec pede justo, fringilla vel, aliquet nec, vulputate eget, arcu. In enim justo, rhoncus ut, imperdiet a, venenatis vitae, justo. Nullam dictum felis eu pede mollis pretium. Integer tincidunt. Cras dapibus. Vivamus elementum semper nisi. Aenean vulputate eleifend</p>
    </div>

    <div class="social" aria-label="Soziale Netzwerke"><span></span><span></span></div>
    <div class="footer-links">
      <span>Kontakt</span><span>|</span><span>Impressum</span><span>|</span>
      <svg width="15" height="15" viewBox="0 0 15 15" aria-label="Suche"><circle cx="6" cy="6" r="4.5" fill="none" stroke="#1b1b1b" stroke-width="2"/><line x1="9.3" y1="9.3" x2="14" y2="14" stroke="#1b1b1b" stroke-width="2.4" stroke-linecap="round"/></svg>
    </div>
  </main>

  <footer class="footer">
    <div class="footer-col" style="left:254px">Lumo Staffing<br>International Promotion &amp; HR Services<br>Geschäftsführer: Marta Lindqvist</div>
    <div class="footer-rule" style="left:469px"></div>
    <div class="footer-col" style="left:481px">Bergblickweg 8<br>83000 Almstadt</div>
    <div class="footer-rule" style="left:612px"></div>
    <div class="footer-col" style="left:621px">Tel.: +49 (0) 80 00 12 34 56 7<br>E-Mail: info@lumo-staffing.de<br>www.lumo-staffing.de</div>
    <div class="footer-rule" style="left:816px"></div>
    <div class="footer-brand">Lumo<br>Staffing</div>
  </footer>
</body>
</html>
```